Business Card Design & Gift cards, Gift Cert, Donation Card

Retail Gift Store-in addition to Business Cards we'd like sequenced 2 sided Gift cards, Gift Certificate Cards, and Donation Cards.please see examples and email for clarificationlogos attached with examples-
Gift Card, Gift Certificate and Donation Card will all be same style just differant upper right title, with back side info as example.
business card, as example is single sided.
looking for additional ideas for layout

Industry/Entity Type

Business

Contact Information for Business Card

211 Newman St.Harlow Bay, WI 48730989.362.8730Office@TinPail.com

Requirements
Must have
• Blue as per example
• Logos provided
• like gradiant background

```html
<!DOCTYPE html>
<html lang="en">
<head>
<meta charset="UTF-8">
<title>Tin Pail – Business Card &amp; Gift Card</title>
<link rel="stylesheet" href="https://fonts.googleapis.com/css2?family=Comic+Neue:wght@400;700&display=swap">
<style>
  :root {
    --page-bg: #e6e6e6;
    --card-bg: #ffffff;
    --ink: #111111;
    --ink-soft: #555555;
    --brand-blue: #1f2fc4;
    --brand-yellow: #f7e43a;
    --rule: #333333;
  }
  * { box-sizing: border-box; margin: 0; padding: 0; }
  html, body { width: 1105px; height: 1200px; overflow: hidden; }
  body {
    background: var(--page-bg);
    font-family: "Comic Neue", "Comic Sans MS", cursive;
    position: relative;
  }
  .card {
    position: absolute;
    left: 196px;
    width: 720px;
    height: 412px;
    background: var(--card-bg);
    border-radius: 26px;
  }
  .card--front { top: 146px; }
  .card--back { top: 602px; }

  /* Front */
  .logo-art {
    position: absolute;
    left: 44px; top: 50px;
    width: 163px; height: 176px;
    background: linear-gradient(160deg, var(--brand-blue) 0%, var(--brand-blue) 60%, var(--brand-yellow) 100%);
    border-radius: 6px;
  }
  .brand-name {
    position: absolute;
    right: 43px; top: 44px;
    font-size: 60px;
    font-weight: 400;
    letter-spacing: 2px;
    color: var(--ink);
    line-height: 1;
  }
  .contact {
    position: absolute;
    left: 44px; top: 250px;
    font-size: 22px;
    color: var(--ink-soft);
    line-height: 28px;
    list-style: none;
  }
  .contact li { display: flex; align-items: center; gap: 8px; }
  .contact .address-2 { margin-bottom: 8px; }
  .contact svg { width: 18px; height: 18px; fill: var(--ink); }
  .contact .email-row { margin-top: 4px; }
  .services {
    position: absolute;
    right: 40px; top: 186px;
    list-style: none;
    text-align: right;
    font-size: 22px;
    line-height: 26.2px;
    color: var(--ink-soft);
  }
  .services li::after {
    content: "•";
    color: var(--ink);
    font-size: 16px;
    margin-left: 10px;
  }

  /* Back */
  .faint-mark {
    position: absolute;
    left: 232px; top: 33px;
    width: 325px; height: 352px;
    background: linear-gradient(170deg, rgba(31,47,196,0.07) 0%, rgba(31,47,196,0.07) 60%, rgba(247,228,58,0.14) 100%);
    border-radius: 12px;
  }
  .card-number {
    position: absolute;
    right: 40px; top: 38px;
    font-size: 18px;
    color: var(--ink);
  }
  .field {
    position: absolute;
    left: 56px;
    right: 42px;
    display: flex;
    align-items: baseline;
    color: var(--ink);
  }
  .field .label { white-space: nowrap; }
  .field .blank {
    flex: 1;
    border-bottom: 1.5px solid var(--rule);
    margin-left: 14px;
    height: 1px;
  }
  .field--large { font-size: 28px; font-weight: 700; right: 52px; }
  .field--to { top: 78px; }
  .field--from { top: 136px; }
  .field--to .blank { margin-left: 36px; }
  .field--small { font-size: 22px; font-weight: 400; }
  .field--issued { top: 224px; }
  .field--expires { top: 272px; }
  .field--employee { top: 320px; }
  .field--employee .blank { margin-left: 22px; }
</style>
</head>
<body>

<section class="card card--front" aria-label="Business card">
  <div class="logo-art" role="img" aria-label="Brand illustration: figure stepping over a rising sun"></div>
  <h1 class="brand-name">TIN PAIL</h1>

  <ul class="contact">
    <li>487 Larkfield Ave.</li>
    <li class="address-2">Harlow Bay, WI 48615</li>
    <li>
      <svg viewBox="0 0 24 24" aria-hidden="true"><path d="M6.6 10.8a15.1 15.1 0 0 0 6.6 6.6l2.2-2.2a1 1 0 0 1 1-.25 11.4 11.4 0 0 0 3.6.6 1 1 0 0 1 1 1V20a1 1 0 0 1-1 1A17 17 0 0 1 3 4a1 1 0 0 1 1-1h3.5a1 1 0 0 1 1 1c0 1.25.2 2.45.57 3.57a1 1 0 0 1-.25 1z"/></svg>
      715.514.2067
    </li>
    <li class="email-row">
      <svg viewBox="0 0 24 24" aria-hidden="true"><path d="M2 5h20v14H2z M3.5 6.5 12 12l8.5-5.5v-.01H3.5z" fill-rule="evenodd"/></svg>
      Office@TinPail.com
    </li>
  </ul>

  <ul class="services">
    <li>Gourmet Food</li>
    <li>Fine Wines</li>
    <li>Gift Baskets</li>
    <li>Kitchen &amp; Bath Accessories</li>
    <li>Candles</li>
    <li>Cards</li>
    <li>Soaps</li>
  </ul>
</section>

<section class="card card--back" aria-label="Gift card back">
  <div class="faint-mark" role="img" aria-label="Faint brand decoration"></div>
  <p class="card-number">Card Number : 58724</p>

  <div class="field field--large field--to"><span class="label">To :</span><span class="blank"></span></div>
  <div class="field field--large field--from"><span class="label">Form :</span><span class="blank"></span></div>

  <div class="field field--small field--issued"><span class="label">Date&nbsp; Issued :</span><span class="blank"></span></div>
  <div class="field field--small field--expires"><span class="label">Expiration Date :</span><span class="blank"></span></div>
  <div class="field field--small field--employee"><span class="label">Employee :</span><span class="blank"></span></div>
</section>

</body>
</html>
```